Hadley & Partners, LLC Business Card 2016

We need a new business card design for a very important trade show coming up.

We are a compliance Consulting Firm. Our clients are stock brokerage firms and investment advisers.

I would like our logo on both sides of the card.

Info in the front of the card shold include:

Logo
First & Last Name
Title
Office #
Cell #
Email
Company Address (42 W. Calloway St., Suite 300 Pasadena, CA 91417

Back of the card should include the logo and url: www.hadleypartnersgroup.com

Target Market(s)

Stock Brokerage Firms and Investment Advisers

Industry/Entity Type

Financial Service

Contact Information for Business Card

Marcus J. Pellew
President
42 W. Calloway St., Suite 300
Pasadena, CA 91417
O 626.555.0147 ext. 204
C 818.555.0193
Email: marcus@hadleypartnersgroup.com
www.hadleypartnersgroup.com

Requirements
Nice to have
• The back of the card could be black with the logo with the white letters.
• I do want the front of the card to at least have the color logo with the black "Hadley & Partners Lettering.

```html
<!DOCTYPE html>
<html lang="en">
<head>
<meta charset="utf-8">
<title>Hadley &amp; Partners – Business Card</title>
<link rel="stylesheet" href="https://fonts.googleapis.com/css2?family=Cinzel:wght@400;700&family=Lato:wght@400&display=swap">
<style>
  :root {
    --bg: #e9e9e9;
    --card-white: #ffffff;
    --card-black: #000000;
    --ink: #111111;
    --red: #c9242a;
    --red-dark: #9e1a1d;
    --steel: #8a8f96;
    --steel-dark: #4f555c;
    --rule: #555555;
  }
  * { margin: 0; padding: 0; box-sizing: border-box; }
  html, body { width: 1200px; height: 466px; overflow: hidden; background: var(--bg); }
  .stage { position: relative; width: 1200px; height: 466px; }
  .card { position: absolute; top: 77px; width: 536px; height: 307px; overflow: hidden; }
  .card-front { left: 46px; background: var(--card-white); }
  .card-back { left: 618px; background: var(--card-black); }
  .corner-shapes { position: absolute; inset: 0; }

  .brand { position: absolute; display: flex; align-items: center; gap: 14px;
    font-family: "Cinzel", serif; font-weight: 700; letter-spacing: 0.02em; white-space: nowrap; }
  .brand-mark { display: block; background: var(--red); }
  .front-brand { left: 24px; top: 30px; font-size: 26px; color: var(--ink); }
  .front-brand .brand-mark { width: 36px; height: 36px; }

  .person { position: absolute; left: 0; width: 256px; top: 160px; text-align: center;
    font-family: "Cinzel", serif; color: var(--ink); }
  .person-name { font-size: 23px; font-weight: 400; letter-spacing: 0.01em; }
  .person-title { font-size: 15px; margin-top: 4px; letter-spacing: 0.04em; }

  .divider { position: absolute; left: 256px; top: 115px; width: 1px; height: 168px; background: var(--rule); }

  .contact { position: absolute; left: 275px; top: 136px; list-style: none;
    font-family: "Lato", sans-serif; font-size: 13.5px; color: var(--ink); line-height: 21px; }
  .contact li { display: flex; align-items: flex-start; gap: 5px; }
  .contact .icon { width: 12px; height: 12px; margin-top: 4px; flex: none; }
  .contact .indent { padding-left: 17px; }
  .contact .gap { margin-top: 13px; }

  .back-brand { left: 0; right: 0; top: 70px; flex-direction: column; gap: 22px;
    color: var(--card-white); font-size: 34px; font-weight: 400; letter-spacing: 0.04em; }
  .back-brand .brand-mark { width: 64px; height: 64px; }
</style>
</head>
<body>
<main class="stage">
  <section class="card card-front" aria-label="Business card front">
    <svg class="corner-shapes" width="536" height="307" viewBox="0 0 536 307" aria-hidden="true">
      <polygon points="449,93 536,0 536,93" fill="var(--red)"/>
      <polygon points="449,93 525,93 536,104 536,196" fill="var(--steel)"/>
      <polygon points="0,231 0,307 70,307" fill="var(--red)"/>
    </svg>

    <div class="brand front-brand"><span class="brand-mark"></span><span class="brand-name">Hadley &amp; Partners</span></div>

    <div class="person">
      <p class="person-name">Marcus Pellew</p>
      <p class="person-title">President</p>
    </div>

    <div class="divider"></div>

    <ul class="contact">
      <li><svg class="icon" viewBox="0 0 12 12"><path d="M6 11.5C3.5 8.3 2.2 6.4 2.2 4.8a3.8 3.8 0 0 1 7.6 0c0 1.6-1.3 3.5-3.8 6.7z" fill="none" stroke="currentColor" stroke-width="1.1"/><circle cx="6" cy="4.8" r="1.4" fill="none" stroke="currentColor" stroke-width="1"/></svg>42 W. Calloway St., Suite 300</li>
      <li class="indent">Pasadena, CA 91417</li>
      <li><svg class="icon" viewBox="0 0 12 12"><circle cx="6" cy="6" r="5.3" fill="none" stroke="currentColor" stroke-width="1"/><path d="M4.2 3.2l1 1.4-.6.8c.4.9 1 1.5 1.9 1.9l.8-.6 1.4 1-.6 1c-2.3-.2-4.3-2.2-4.5-4.5z" fill="currentColor"/></svg>O 626.555.0147 ext.204</li>
      <li class="indent">C 818.555.0193</li>
      <li class="gap"><svg class="icon" viewBox="0 0 12 12"><g fill="none" stroke="currentColor" stroke-width="0.9"><circle cx="6" cy="6" r="5.2"/><ellipse cx="6" cy="6" rx="2.3" ry="5.2"/><path d="M0.8 6h10.4M1.6 3.3h8.8M1.6 8.7h8.8"/></g></svg>marcus@hadleypartnersgroup.com</li>
      <li><svg class="icon" viewBox="0 0 12 12"><rect x="0.5" y="2.5" width="11" height="7.5" fill="currentColor"/><path d="M0.8 2.9L6 7l5.2-4.1" fill="none" stroke="#fff" stroke-width="0.9"/></svg>www.hadleypartnersgroup.com</li>
    </ul>
  </section>

  <section class="card card-back" aria-label="Business card back">
    <div class="brand back-brand"><span class="brand-mark"></span><span class="brand-name">Hadley &amp; Partners</span></div>
  </section>
</main>
</body>
</html>
```